Business card design for Velvet Harbor

We need business cards designed for our new marketing consulting company, Velvet Harbor. Our services include marketing strategy, go-to-market and launch planning, growth strategy, and execution. We serve medical technology and health technology companies, from startups to well-established growth companies.

The business cards should feel professional, credible, reliable and trustworthy, and should instill confidence. Also bold, creative, and modern.

The design must use the Velvet Harbor logo.

The primary brand color is this orange: #FF5501
A secondary color that you can use is this gray: #282B2D
I would prefer only to use the orange and gray. But if you feel you really need an additional accent color (please use it very sparingly, as little as possible), you can use this blue for small accent purposes: #009FED

Attached are the logo files. The main logo is the one with a little bit of orange on the left and the rest is gray.

The business card should include the following:

Velvet Harbor logo
First name and last name
Title
Email address
Phone number and type (in whatever order looks best for the design
Website (the website does not need to be in the same block as the personal info)

For example:

Nessa Pryle
Founder & Principal
nessa@velvetharbor.com
+1.628.309.4156 mobile (can use "." or spaces in between blocks of numbers)
velvetharbor.com (somewhere on the card, it does not need to be with the personal info; and note that there is no "www." at the beginning)

Note that there will be no address listed on the business card.

Target Market(s)

Executives (CEO, head of marketing, head of sales) at medical technology and health technology companies, mostly in their 40s and older, well-educated, often with advanced degrees. They are strategic thinkers, responsible for budgets, and familiar with P&L. Their comfort with and trust in using outside consultants varies.

Industry/Entity Type

Medical technology and health technology companies.

Contact Information for Business Card

See project description

Font styles to use
Sans Serif

Requirements
Must have
• Logo and see Business card details section above.

```html
<!DOCTYPE html>
<html lang="en">
<head>
<meta charset="utf-8">
<title>Velvet Harbor — Business Card</title>
<link rel="stylesheet" href="https://fonts.googleapis.com/css2?family=Montserrat:wght@400;600;700&display=swap">
<style>
  :root {
    --orange: #d8521f;
    --charcoal: #222527;
    --text-light: #e4e4e4;
    --backdrop: #e6e6e6;
  }
  * { margin: 0; padding: 0; box-sizing: border-box; }
  html, body {
    width: 1200px; height: 1200px; overflow: hidden;
    background: var(--backdrop);
    font-family: "Montserrat", sans-serif;
  }
  .card {
    position: absolute; left: 248px;
    width: 704px; height: 402px;
    background: var(--charcoal);
    border-radius: 4px; overflow: hidden;
  }
  .card--front { top: 130px; }
  .card--back {
    top: 590px;
    display: flex; align-items: center; justify-content: center;
  }

  .front-panel { position: absolute; inset: 0; }

  .person-name {
    position: absolute; left: 38px; top: 50px;
    font-size: 30px; font-weight: 700; color: var(--orange);
    letter-spacing: 0.2px; line-height: 1.2;
  }
  .person-title {
    position: absolute; left: 39px; top: 92px;
    font-size: 17px; font-weight: 400; color: var(--text-light);
  }
  .contact-list {
    position: absolute; left: 38px; top: 280px;
    list-style: none;
  }
  .contact-item {
    display: flex; align-items: center; gap: 9px;
    height: 27px;
    font-size: 17px; color: var(--text-light);
  }
  .contact-icon { width: 16px; height: 16px; flex: none; }

  .wordmark {
    display: flex; align-items: center; gap: 40px;
  }
  .wordmark-dot {
    width: 22px; height: 22px; border-radius: 50%;
    background: var(--orange);
  }
  .wordmark-name {
    font-size: 45px; font-weight: 600; color: var(--text-light);
    line-height: 50px; letter-spacing: 15px; text-transform: uppercase;
  }
</style>
</head>
<body>

<section class="card card--front" aria-label="Business card front">
  <svg class="front-panel" width="704" height="402" viewBox="0 0 704 402" aria-hidden="true">
    <defs>
      <linearGradient id="paperTone" x1="0" y1="0" x2="1" y2="1">
        <stop offset="0" stop-color="#f7f7f7"/>
        <stop offset="1" stop-color="#e4e4e4"/>
      </linearGradient>
    </defs>
    <rect x="503" y="0" width="201" height="402" fill="url(#paperTone)"/>
    <circle cx="503" cy="200" r="219" fill="url(#paperTone)"/>
  </svg>

  <h1 class="person-name">Nessa Pryle</h1>
  <p class="person-title">Founder &amp; Principal</p>

  <ul class="contact-list">
    <li class="contact-item">
      <svg class="contact-icon" viewBox="0 0 16 16" aria-hidden="true">
        <path fill="var(--orange)" d="M3.6 1.5l2.2 2.6-1.3 1.6c.8 1.9 2.2 3.3 4 4.1l1.6-1.3 2.6 2.2-1.3 2.3c-4.9-.3-8.9-4.3-9.2-9.2z"/>
        <path fill="none" stroke="var(--orange)" stroke-width="1.2" d="M9.5 2.5a4 4 0 0 1 4 4M9.5 0.8a5.7 5.7 0 0 1 5.7 5.7"/>
      </svg>
      <span>+1.628.309.4156 mobile</span>
    </li>
    <li class="contact-item">
      <svg class="contact-icon" viewBox="0 0 16 16" aria-hidden="true">
        <rect x="0.5" y="3" width="15" height="10.5" rx="1" fill="var(--orange)"/>
        <path d="M1.5 4.2l6.5 5 6.5-5" fill="none" stroke="var(--charcoal)" stroke-width="1.3"/>
      </svg>
      <span>nessa@velvetharbor.com</span>
    </li>
    <li class="contact-item">
      <svg class="contact-icon" viewBox="0 0 16 16" aria-hidden="true">
        <circle cx="8" cy="8" r="7.5" fill="var(--orange)"/>
        <g fill="none" stroke="var(--charcoal)" stroke-width="1.1">
          <ellipse cx="8" cy="8" rx="3" ry="7.2"/>
          <path d="M0.6 8h14.8M8 0.6v14.8"/>
        </g>
      </svg>
      <span>velvetharbor.com</span>
    </li>
  </ul>
</section>

<section class="card card--back" aria-label="Business card back">
  <div class="wordmark">
    <span class="wordmark-dot" aria-hidden="true"></span>
    <p class="wordmark-name">Velvet<br>Harbor</p>
  </div>
</section>

</body>
</html>
```